make our generated pages look good ( HTML ONLY)

Our application http://www.taskweave.com.au has many server side generated screens.

We wish to improve the look of these generated screens, please see attached html pages and screen shots.

Your improved look will be ported back to our screen generator so we really looking for "less is more". We really want the improved look to be based on the html pages attached so that we will be able to see the necessary changes required to our screen generator to make the same look.

We want the screens to be adaptable to different screen sizes and applicable to tablets and desktops ( maybe even phones).

**** PLEASE FOCUS ON THE CONTACT SCREEN ****
Updates

I've marked the project as "guaranteed".

**** Please note I'm expecting the attached pages to be returned looking better/more modern. See http://www.plovercode.com.au for some colors.

My goal is to be able to do a difference on the existing page and the ones that is returned so that I can make the changes to generate the pages using the better looking theme.

For the sections the fieldset/legend used for http://mrvl.taskweave.com.au/login look nice to me. Of course they need to work on all the browsers thou. 

The sections in the contact screen can be made nicer by rounding the corners.

Here are two samples :-

1. used by pixel harbour
2. used on our login page.

We use wix-dlq in our places in our application so themes/css/images from wix-dlq explorer will fit in well.

Target Market(s)

Sustainable Technology is our tag line

Requirements
Must have
• **** I WANT THE HTML PAGE BACK BUT LOOKING BETTER *****

1) Convert the attach server side generated HTML pages to be more controlled by css ( no server coding we will do that once we have a nice look)

2) We need to be able to make the same simple changes to the screen generator
Nice to have
• We would like the screens to be skinable by simply changing CSS

This is a "less is more" project, we want someone with a good eye to make these two sample pages look much nicer
Should not have
• restricted license. Any images used ( prefer no or limited images ) must be public

```html
<!DOCTYPE html>
<html lang="en">
<head>
<meta charset="utf-8">
<title>Contact – Details</title>
<link href="https://fonts.googleapis.com/css2?family=Arimo:wght@400;700&display=swap" rel="stylesheet">
<style>
  :root {
    --page-bg: #ffffff;
    --toolbar-top: #f4f4f4;
    --toolbar-bottom: #dcdcdc;
    --toolbar-line: #b9b9b9;
    --btn-top: #e9e9e9;
    --btn-bottom: #c9c9c9;
    --btn-border: #8d8d8d;
    --btn-text: #6a6a6a;
    --tab-dark: #262626;
    --tab-divider: #555555;
    --tab-active-top: #3b86d4;
    --tab-active-bottom: #2262b3;
    --section-blue: #2259a8;
    --section-line: #173f7c;
    --body-bg: #f7f7f7;
    --panel-border: #9a9a9a;
    --label: #333333;
    --input-border: #7d7d7d;
    --select-top: #e4e4e4;
    --select-bottom: #b9b9b9;
    --white: #ffffff;
    --grid-head: #333333;
    --accent-blue: #3a7bd5;
  }
  * { box-sizing: border-box; margin: 0; padding: 0; }
  html, body { width: 928px; height: 1200px; overflow: hidden; background: var(--page-bg); }
  body { font-family: "Arimo", Arial, sans-serif; color: var(--label); }

  .screen { width: 960px; height: 1242px; position: relative; transform: scale(0.966667); transform-origin: 0 0; }

  .toolbar { position: absolute; left: 0; top: 0; width: 960px; height: 51px;
    background: linear-gradient(var(--toolbar-top), var(--toolbar-bottom));
    border-bottom: 1px solid var(--toolbar-line); }
  .tool-btn { position: absolute; top: 12px; height: 26px; border: 1px solid var(--btn-border);
    border-radius: 4px; background: linear-gradient(var(--btn-top), var(--btn-bottom));
    font: 700 13px "Arimo", Arial, sans-serif; color: var(--btn-text);
    display: flex; align-items: center; justify-content: center; }

  .panel { position: absolute; left: 10px; top: 70px; width: 940px; height: 1180px;
    border: 1px solid var(--panel-border); border-top: none; background: var(--body-bg); }

  .tabs { display: flex; height: 33px; background: var(--tab-dark); border-radius: 4px 4px 0 0; overflow: hidden; }
  .tab { flex: 1; display: flex; align-items: center; justify-content: center; color: var(--white);
    font-size: 16px; border-left: 1px solid var(--tab-divider); }
  .tab:first-child { border-left: none; }
  .tab.is-active { background: linear-gradient(var(--tab-active-top), var(--tab-active-bottom)); }

  .section-head { position: absolute; left: -1px; width: 940px; height: 41px;
    background: var(--section-blue); border-top: 1px solid var(--section-line); border-bottom: 1px solid var(--section-line);
    color: var(--white); font-size: 17px; padding-left: 10px; display: flex; align-items: center; }

  .label { position: absolute; font-size: 17px; line-height: 20px; color: var(--label); white-space: nowrap; }
  .input { position: absolute; width: 161px; height: 26px; background: var(--white);
    border: 1px solid var(--input-border); border-radius: 5px; font-size: 12px; padding-left: 9px;
    display: flex; align-items: center; color: #222; }
  .input.tall { height: 50px; }
  .select { position: absolute; width: 161px; height: 30px; border: 1px solid #9c9c9c; border-radius: 3px;
    background: linear-gradient(var(--select-top), var(--select-bottom)); }
  .select::after { content: ""; position: absolute; right: 6px; top: 12px;
    border-left: 5px solid transparent; border-right: 5px solid transparent; border-top: 5px solid #222; }
  .select.title { width: 50px; font-size: 17px; color: #444; padding-left: 7px; display: flex; align-items: center; }
  .select.title::after { right: 6px; top: 13px; border-top-color: #333; }
  .pill { position: absolute; width: 60px; height: 25px; border: 1px solid #8a8a8a; border-radius: 13px;
    background: linear-gradient(#efefef, #c7c7c7); font-size: 13px; color: #444;
    display: flex; align-items: center; justify-content: center; }

  .category-grid { position: absolute; left: 140px; top: 1060px; width: 160px; border: 1px solid #555; font-size: 12.5px; }
  .category-grid .grid-head { background: var(--grid-head); color: var(--white); height: 20px; padding-left: 3px; line-height: 20px; }
  .category-grid .grid-row { height: 20px; padding-left: 3px; line-height: 19px; border-top: 1px solid #555;
    background: var(--white); color: #333; position: relative; }
  .grid-row .marker { position: absolute; right: 5px; top: 5px; width: 9px; height: 9px; border: 1px solid #333;
    border-radius: 2px; background: #999; }
  .grid-row .marker.is-on { background: var(--accent-blue); }
</style>
</head>
<body>
<div class="screen">
  <nav class="toolbar">
    <div class="tool-btn" style="left:10px;width:40px">Ok</div>
    <div class="tool-btn" style="left:70px;width:60px">Apply</div>
    <div class="tool-btn" style="left:150px;width:60px">Delete</div>
    <div class="tool-btn" style="left:230px;width:70px">Refresh</div>
    <div class="tool-btn" style="left:320px;width:50px">Print</div>
    <div class="tool-btn" style="left:390px;width:60px">Close</div>
    <div class="tool-btn" style="left:470px;width:80px">Go Back</div>
  </nav>

  <main class="panel">
    <div class="tabs">
      <div class="tab is-active">Details</div>
      <div class="tab">Misc</div>
      <div class="tab">Info</div>
      <div class="tab">Log</div>
    </div>

    <!-- Contact information -->
    <div class="section-head" style="top:33px">Contact Information:</div>

    <div class="label" style="left:10px;top:107px">Title:</div>
    <div class="select title" style="left:140px;top:100px">Mr</div>
    <div class="label" style="left:10px;top:155px">First Name:</div>
    <div class="input" style="left:139px;top:153px"></div>
    <div class="label" style="left:10px;top:206px">Last Name:</div>
    <div class="input" style="left:139px;top:203px"></div>
    <div class="label" style="left:10px;top:257px">Business Unit:</div>
    <div class="input" style="left:139px;top:254px"></div>
    <div class="pill" style="left:310px;top:255px;width:70px">Search</div>
    <div class="pill" style="left:390px;top:255px">View</div>
    <div class="label" style="left:10px;top:308px">Work Phone:</div>
    <div class="input" style="left:139px;top:305px"></div>
    <div class="label" style="left:10px;top:359px">Mobile:</div>
    <div class="input" style="left:139px;top:356px">418507216</div>
    <div class="label" style="left:10px;top:410px">SMS Mobile:</div>
    <div class="input" style="left:139px;top:407px"></div>
    <div class="label" style="left:10px;top:461px">Email:</div>
    <div class="input" style="left:139px;top:458px"></div>
    <div class="label" style="left:10px;top:512px">Fax:</div>
    <div class="input" style="left:139px;top:509px"></div>

    <div class="label" style="left:480px;top:106px">Department:</div>
    <div class="input" style="left:609px;top:103px"></div>
    <div class="label" style="left:480px;top:155px">Job Title:</div>
    <div class="input" style="left:609px;top:153px"></div>
    <div class="label" style="left:480px;top:206px">Reports To:</div>
    <div class="select" style="left:610px;top:202px"></div>
    <div class="pill" style="left:780px;top:205px">View</div>
    <div class="label" style="left:480px;top:257px">Home Phone:</div>
    <div class="input" style="left:609px;top:254px"></div>
    <div class="label" style="left:480px;top:308px">Web:</div>
    <div class="input" style="left:609px;top:305px"></div>
    <div class="label" style="left:480px;top:359px">Enquiry Source:</div>
    <div class="select" style="left:610px;top:355px"></div>
    <div class="pill" style="left:780px;top:358px">Edit</div>
    <div class="label" style="left:480px;top:410px">Account Mgr:</div>
    <div class="select" style="left:610px;top:406px"></div>
    <div class="pill" style="left:780px;top:409px">View</div>
    <div class="label" style="left:480px;top:461px">Contact#:</div>
    <div class="input" style="left:609px;top:458px"></div>

    <!-- Address details -->
    <div class="section-head" style="top:579px">Address Details:</div>

    <div class="label" style="left:10px;top:643px">Address:</div>
    <div class="input tall" style="left:139px;top:640px"></div>
    <div class="label" style="left:10px;top:707px">Suburb/City:</div>
    <div class="input" style="left:139px;top:704px"></div>
    <div class="label" style="left:10px;top:747px">Postcode:</div>
    <div class="input" style="left:139px;top:744px"></div>
    <div class="label" style="left:10px;top:789px">Country:</div>
    <div class="select" style="left:140px;top:785px"></div>
    <div class="label" style="left:10px;top:834px">State/Region:</div>
    <div class="select" style="left:140px;top:830px"></div>

    <div class="label" style="left:480px;top:643px">Postal Address:</div>
    <div class="input tall" style="left:609px;top:640px"></div>
    <div class="label" style="left:480px;top:707px">Suburb/City:</div>
    <div class="input" style="left:609px;top:704px"></div>
    <div class="label" style="left:480px;top:747px">Postcode:</div>
    <div class="input" style="left:609px;top:744px"></div>
    <div class="label" style="left:480px;top:789px">Country:</div>
    <div class="select" style="left:610px;top:785px"></div>
    <div class="label" style="left:480px;top:834px">State/Region:</div>
    <div class="select" style="left:610px;top:830px"></div>

    <!-- Classification -->
    <div class="section-head" style="top:909px">Classification:</div>

    <div class="label" style="left:10px;top:974px">Position Class:</div>
    <div class="select" style="left:140px;top:970px"></div>
    <div class="label" style="left:10px;top:1021px">Revenue:</div>
    <div class="input" style="left:139px;top:1018px"></div>
    <div class="label" style="left:10px;top:1062px">Categories:</div>
    <div class="category-grid">
      <div class="grid-head">Name</div>
      <div class="grid-row">Business Partner<span class="marker"></span></div>
      <div class="grid-row">Business Partner<span class="marker is-on"></span></div>
    </div>
    <div class="pill" style="left:140px;top:1130px">Add</div>

    <div class="label" style="left:480px;top:974px">Industry:</div>
    <div class="select" style="left:610px;top:970px"></div>
    <div class="label" style="left:480px;top:1018px">Sub Industry:</div>
    <div class="select" style="left:610px;top:1014px"></div>
  </main>
</div>
</body>
</html>
```